ページ構成は
・トップページ
・代表メッセージ
・企業情報
・合同会社とは?
・採用情報_一覧
・採用情報_詳細
・サンクスページ(採用)
・サンクスページ(見積もり)
を想定しています。

ワイヤーはTOP以外は現在作成中です。
提案時に、下層ページの概算見積を出して頂けると助かります。
1ページ
希望する色は決まっていませんが、弊社のロゴはオレンジです。
ロゴを添付します。

全体の雰囲気や、強調すべき点を抑えていただいた点が良かったです。

ご提案ありがとうございました。
良いデザインが多く、そのうち3人の方で特に悩むほどでした。
またの機会があればぜひご提案頂けますと幸いです。

```html
<!DOCTYPE html>
<html lang="ja">
<head>
<meta charset="utf-8">
<title>ミナトワ合同会社</title>
<link href="https://fonts.googleapis.com/css2?family=Noto+Sans+JP:wght@400;500;700&family=Roboto:wght@300;400&display=swap" rel="stylesheet">
<style>
:root{
  --orange:#f0893e;
  --orange-soft:#f6a66a;
  --ink:#333333;
  --ink-soft:#666666;
  --line:#bfbfbf;
  --bg:#ffffff;
  --bg-grey:#f1f1f1;
  --footer-bar:#4a4250;
  --hero-a:#3d4f66;
  --hero-b:#8b9bb0;
}
*{margin:0;padding:0;box-sizing:border-box}
html,body{width:1200px;height:5168px;overflow:hidden}
body{font-family:"Noto Sans JP",sans-serif;color:var(--ink);background:var(--bg);position:relative}
.abs{position:absolute}
.hero{left:0;top:0;width:1200px;height:580px;background:linear-gradient(160deg,var(--hero-a),var(--hero-b) 55%,#c9cfd8)}
.site-header{left:0;top:0;width:1200px;height:64px;display:flex;align-items:center;padding:0 40px}
.brand{display:flex;align-items:center;gap:10px;color:#fff;font-weight:700;font-size:16px}
.brand-mark{width:34px;height:34px;background:var(--orange)}
.nav{margin-left:auto;display:flex;gap:0}
.nav a{color:#fff;text-decoration:none;font-size:14px;padding:10px 34px;border-left:1px solid rgba(255,255,255,.5)}
.nav a.nav-cta{border:1px solid #fff;margin-left:20px}
.hero-title{left:0;top:218px;width:1200px;text-align:center;color:#fff;font-size:40px;font-weight:500;letter-spacing:.06em;text-shadow:0 2px 6px rgba(0,0,0,.3)}
.btn-orange{left:490px;top:398px;width:310px;height:58px;background:var(--orange);color:#fff;font-size:18px;font-weight:700;display:flex;align-items:center;justify-content:center;border-radius:3px}
.hero-sub{left:0;top:484px;width:1200px;text-align:center;color:#fff;font-size:20px;text-shadow:0 1px 4px rgba(0,0,0,.4)}
.h2{left:0;width:1200px;text-align:center;font-size:26px;font-weight:700;letter-spacing:.05em}
.h2::after{content:"";display:block;width:60px;height:2px;background:var(--orange);margin:14px auto 0}
.lead-text{left:160px;width:880px;font-size:14px;line-height:2;color:var(--ink-soft);text-align:center}
.reason-band{left:0;width:1200px;height:400px}
.band-1{top:1100px;background:linear-gradient(100deg,#9aa3ad,#dfe2e6 45%,#bfc5cc)}
.band-2{top:1540px;background:linear-gradient(100deg,#6d6863,#c9c4bd 50%,#8e8a86)}
.band-3{top:1960px;background:linear-gradient(100deg,#e9e9e9,#c9ccd0 60%,#9ca2a8)}
.reason-card{width:800px;background:rgba(255,255,255,.93);padding:30px 40px 34px;box-shadow:0 4px 14px rgba(0,0,0,.12)}
.reason-head{display:flex;align-items:center;gap:26px;border-bottom:1px solid var(--line);padding-bottom:18px}
.reason-num{font-family:"Roboto",sans-serif;font-weight:300;font-size:82px;line-height:1;color:#555;font-style:italic}
.reason-title{font-size:24px;font-weight:700;line-height:1.5}
.reason-why{font-size:18px;font-weight:500;color:var(--ink)}
.reason-body{margin-top:18px;font-size:14px;line-height:2;color:var(--ink-soft)}
.btn-outline{border:1px solid #888;display:flex;align-items:center;justify-content:center;font-size:16px;color:var(--ink);background:#fff}
.btn-outline svg{margin-left:18px}
.service-band{left:0;top:2700px;width:1200px;height:640px;background:var(--bg-grey)}
.service-card{top:2740px;width:420px;height:580px;background:#fff;padding:32px 30px;box-shadow:0 2px 10px rgba(0,0,0,.08)}
.service-title{font-size:22px;font-weight:700}
.service-title small{font-size:13px;font-weight:400;color:var(--ink-soft);margin-left:8px}
.service-title::after{content:"";display:block;width:40px;height:2px;background:var(--orange);margin-top:10px}
.checks{list-style:none;margin-top:28px}
.checks li{display:flex;gap:10px;font-size:14px;line-height:1.7;margin-bottom:14px}
.checks li svg{flex:none;margin-top:4px}
.service-text{font-size:13px;line-height:1.9;color:var(--ink-soft);margin-top:36px}
.service-btn{position:absolute;left:30px;bottom:32px;width:360px;height:56px;font-size:15px}
.message-banner{left:168px;top:3580px;width:864px;height:120px;background:linear-gradient(90deg,#7a4a2a,#b07a4e 60%,#8a5836)}
.message-label{left:168px;top:3580px;width:864px;height:120px;display:flex;align-items:center;justify-content:center}
.message-label span{background:rgba(255,255,255,.92);padding:10px 40px;font-size:17px;font-weight:500}
.about-btn{top:3720px;width:268px;height:80px;font-size:16px}
.form-intro{left:0;top:3996px;width:1200px;text-align:center;font-size:14px;color:var(--ink-soft)}
.field{left:200px;width:800px}
.field-label{font-size:14px;display:flex;align-items:center;gap:8px}
.req{background:#d9534f;color:#fff;font-size:11px;padding:1px 7px;border-radius:2px}
.field-input{margin-top:8px;height:46px;border:1px solid #aaa;background:#fff}
.field-area{margin-top:8px;height:160px;border:1px solid #aaa;background:#fff}
.submit{left:400px;top:4790px;width:400px;height:64px;background:#cfcfcf;color:#fff;font-size:18px;display:flex;align-items:center;justify-content:center;letter-spacing:.2em}
.site-footer{left:0;top:4900px;width:1200px;height:228px;background:var(--bg-grey);border-top:1px solid #ddd}
.footer-name{left:200px;top:4960px;font-size:24px;font-weight:500}
.footer-address{left:200px;top:5010px;font-size:13px;line-height:1.8;color:var(--ink-soft)}
.footer-nav{left:680px;top:4966px;display:flex;gap:48px;font-size:14px}
.footer-bar{left:0;top:5128px;width:1200px;height:40px;background:var(--footer-bar);color:#ddd;font-size:12px;display:flex;align-items:center;padding-left:200px}
</style>
</head>
<body>

<div class="abs hero" role="img" aria-label="会議テーブルで手を合わせるビジネスチームの写真"></div>
<header class="abs site-header">
  <div class="brand"><span class="brand-mark"></span>ミナトワ</div>
  <nav class="nav">
    <a>企業概要</a><a>合同会社とは?</a><a>採用情報</a><a class="nav-cta">ご相談・お見積もり</a>
  </nav>
</header>
<h1 class="abs hero-title">開発から運用のご相談まで、すべて対応できます。</h1>
<div class="abs btn-orange">ご相談はこちら</div>
<p class="abs hero-sub">運用からでも大丈夫です。お気軽にお問い合わせください。</p>

<h2 class="abs h2" style="top:680px">問題の根本を解決するシステムを開発します。</h2>
<p class="abs lead-text" style="top:770px">お客様の業務を丁寧にお伺いし、課題の原因を見極めたうえで最適な仕組みをご提案します。表面的な対処ではなく、長く使い続けられるシステムづくりを大切にしています。小さなお悩みからでもお気軽にご相談ください。</p>

<h2 class="abs h2" style="top:980px">ミナトワの強みとその理由</h2>

<div class="abs reason-band band-1" role="img" aria-label="ノートパソコンで作業するオフィスの写真"></div>
<div class="abs reason-card" style="left:160px;top:1140px">
  <div class="reason-head"><span class="reason-num">01</span><div><div class="reason-title">費用を安くおさえられる</div><div class="reason-why">理由：常に最新の技術にキャッチアップしているからです。</div></div></div>
  <p class="reason-body">新しい技術を積極的に取り入れることで、開発の手間を減らし、費用を抑えたご提案が可能です。効率の良い手法を選び、無駄のない開発を行います。</p>
</div>

<div class="abs reason-band band-2" role="img" aria-label="打ち合わせをするビジネスパーソンの写真"></div>
<div class="abs reason-card" style="left:240px;top:1580px">
  <div class="reason-head"><span class="reason-num">02</span><div><div class="reason-title">最善な仕様や要件・システムを一緒に定義できる</div><div class="reason-why">理由：着手前にヒアリングを徹底しているからです。</div></div></div>
  <p class="reason-body">開発を始める前に業務の流れや目的をしっかりお聞きし、本当に必要な機能を一緒に整理します。認識のずれを防ぎ、納得のいく形で進めます。</p>
</div>

<div class="abs reason-band band-3" role="img" aria-label="握手をするビジネスパーソンの写真"></div>
<div class="abs reason-card" style="left:160px;top:2000px">
  <div class="reason-head"><span class="reason-num">03</span><div><div class="reason-title">システムの品質が安定している</div><div class="reason-why">理由：少数精鋭のチーム体制だからです。</div></div></div>
  <p class="reason-body">経験豊富なメンバーが少人数で担当するため、情報共有がスムーズで品質のばらつきがありません。完成後も安心してお使いいただけます。</p>
</div>

<div class="abs btn-outline" style="left:400px;top:2420px;width:400px;height:76px">無料でご相談<svg width="40" height="10" viewBox="0 0 40 10"><path d="M0 8h38l-8-6" fill="none" stroke="#555" stroke-width="1.5"/></svg></div>

<h2 class="abs h2" style="top:2572px">ミナトワのサービス</h2>
<div class="abs service-band"></div>

<div class="abs service-card" style="left:168px">
  <div class="service-title">成果型契約<small>(例) こんな方におすすめです。</small></div>
  <ul class="checks">
    <li><svg width="14" height="14"><path d="M2 7l3 3 7-8" fill="none" stroke="#f0893e" stroke-width="2"/></svg>自社オリジナルの顧客管理システムを作りたい</li>
    <li><svg width="14" height="14"><path d="M2 7l3 3 7-8" fill="none" stroke="#f0893e" stroke-width="2"/></svg>指定通りに動くECサイトの管理システムに、新しい決済機能を追加したい</li>
    <li><svg width="14" height="14"><path d="M2 7l3 3 7-8" fill="none" stroke="#f0893e" stroke-width="2"/></svg>紙やExcelによる在庫管理が限界なので、スムーズに在庫管理ができるシステムを作りたい</li>
  </ul>
  <p class="service-text">完成した成果物に対して費用をお支払いいただく契約です。事前に範囲と金額を決めるため、予算の見通しが立てやすくなります。</p>
  <div class="btn-outline service-btn">詳細・お見積もりはこちら<svg width="30" height="10" viewBox="0 0 30 10"><path d="M0 8h28l-8-6" fill="none" stroke="#555" stroke-width="1.5"/></svg></div>
</div>

<div class="abs service-card" style="left:612px">
  <div class="service-title">時間契約<small>(例) こんな方におすすめです。</small></div>
  <ul class="checks">
    <li><svg width="14" height="14"><path d="M2 7l3 3 7-8" fill="none" stroke="#f0893e" stroke-width="2"/></svg>既存システムのメンテナンスを行う人がいなくなった方や、少しの修正、検索や改修をしてほしい方</li>
    <li><svg width="14" height="14"><path d="M2 7l3 3 7-8" fill="none" stroke="#f0893e" stroke-width="2"/></svg>事業拡大や業務効率化に伴い、システムを導入したい方</li>
    <li><svg width="14" height="14"><path d="M2 7l3 3 7-8" fill="none" stroke="#f0893e" stroke-width="2"/></svg>現在動いている開発を迅速に進めたい方</li>
  </ul>
  <p class="service-text">作業した時間に応じて費用をお支払いいただく契約です。内容が固まっていない段階でも柔軟に対応でき、継続的なご依頼に向いています。</p>
  <div class="btn-outline service-btn">詳細・お見積もりはこちら<svg width="30" height="10" viewBox="0 0 30 10"><path d="M0 8h28l-8-6" fill="none" stroke="#555" stroke-width="1.5"/></svg></div>
</div>

<h2 class="abs h2" style="top:3460px">私たちについて</h2>
<div class="abs message-banner" role="img" aria-label="代表者のポートレート写真"></div>
<div class="abs message-label"><span>代表メッセージ</span></div>
<div class="abs btn-outline about-btn" style="left:168px">合同会社とは?<svg width="30" height="10" viewBox="0 0 30 10"><path d="M0 8h28l-8-6" fill="none" stroke="#555" stroke-width="1.5"/></svg></div>
<div class="abs btn-outline about-btn" style="left:466px">企業概要<svg width="30" height="10" viewBox="0 0 30 10"><path d="M0 8h28l-8-6" fill="none" stroke="#555" stroke-width="1.5"/></svg></div>
<div class="abs btn-outline about-btn" style="left:764px">採用情報<svg width="30" height="10" viewBox="0 0 30 10"><path d="M0 8h28l-8-6" fill="none" stroke="#555" stroke-width="1.5"/></svg></div>

<h2 class="abs h2" style="top:3880px">お問い合わせ・ご相談</h2>
<p class="abs form-intro">どんなことでもご相談・ご質問をお待ちしております。ご依頼にお答えいたします。</p>

<div class="abs field" style="top:4040px"><div class="field-label">法人名<span class="req">必須</span></div><div class="field-input"></div></div>
<div class="abs field" style="top:4140px"><div class="field-label">担当者名<span class="req">必須</span></div><div class="field-input"></div></div>
<div class="abs field" style="top:4240px"><div class="field-label">担当者名（ふりがな）</div><div class="field-input"></div></div>
<div class="abs field" style="top:4340px"><div class="field-label">電話番号<span class="req">必須</span></div><div class="field-input"></div></div>
<div class="abs field" style="top:4440px"><div class="field-label">メールアドレス<span class="req">必須</span></div><div class="field-input"></div></div>
<div class="abs field" style="top:4540px"><div class="field-label">お問い合わせ内容<span class="req">必須</span></div><div class="field-area"></div></div>
<div class="abs submit">送信</div>

<footer class="abs site-footer"></footer>
<div class="abs footer-name">ミナトワ合同会社</div>
<div class="abs footer-address">〒100-0000 東京都架空区見本町1丁目2-3<br>TEL 000-0000-0000</div>
<div class="abs footer-nav"><span>企業概要</span><span>合同会社とは?</span><span>採用情報</span></div>
<div class="abs footer-bar">minatowa © All rights reserved.</div>

</body>
</html>
```